Financial Services General Marketing Brochure

Need a brochure to help recipients understand what makes BHC unique and the services that we offer. Must match look/feel of website https://bellhavencustodial.example Layouts should make it easy to read the content - content should not be crammed into a traditional size/layout. Please see attached creative brief for specifics.

Target Market(s)

Financial advisors and mature couples looking for trustee services.

Industry/Entity Type

Financial Service

Colors
34a7d8
ffc214

Requirements
Must have
• See Creative Brief

```html
<!DOCTYPE html>
<html lang="en">
<head>
<meta charset="utf-8">
<title>Bellhaven Custodial – Brochure</title>
<link rel="stylesheet" href="https://fonts.googleapis.com/css2?family=Alegreya+Sans:wght@400;500;700&family=Alegreya:ital,wght@0,500;1,400&display=swap">
<style>
:root{
  --stage:#3a3a3c;
  --navy:#2b4a5a;
  --navy-deep:#26434f;
  --slate:#4a6d8c;
  --ink:#3f6180;
  --orange:#f08a24;
  --amber:#f6ab1f;
  --cream:#f6f1e4;
  --white:#ffffff;
}
*{margin:0;padding:0;box-sizing:border-box}
html,body{width:1185px;height:1200px;overflow:hidden;background:var(--stage)}
body{position:relative;font-family:"Alegreya Sans",sans-serif;color:var(--ink)}
.panel{position:absolute;width:429px;height:429px;background:var(--white);overflow:hidden}
.panel--cover{left:149px;top:155px}
.panel--story{left:607px;top:155px}
.panel--team{left:149px;top:615px}
.panel--services{left:607px;top:615px}
.abs{position:absolute}
.brand-name{font-family:"Alegreya Sans",sans-serif;font-weight:700;color:var(--slate);line-height:1}
.accent-bar{position:absolute;left:0;right:0;bottom:0;height:10px;background:linear-gradient(90deg,var(--orange),var(--amber))}

/* Cover */
.cover-photo{left:0;top:107px;width:429px;height:252px;background:linear-gradient(135deg,#f3a326 0%,#e8891c 45%,#b8651a 75%,#e49a2a 100%)}
.cover-brand{left:276px;top:0;width:128px;height:138px;background:var(--white);display:flex;flex-direction:column;align-items:center;justify-content:flex-end;padding-bottom:14px;gap:8px}
.cover-brand .dot{width:30px;height:30px;border-radius:50%;background:var(--orange)}
.cover-brand .brand-name{font-size:19px;text-align:center}
.cover-tagline{left:0;right:0;top:375px;text-align:center;font-weight:500;font-size:16.5px;line-height:1.15;color:var(--slate)}
.cover-url{left:0;right:0;top:417px;text-align:center;font-size:6px;letter-spacing:3px;color:var(--orange);font-weight:700}

/* Story */
.story-band{left:0;top:0;width:429px;height:187px;background:var(--navy)}
.story-photo{left:180px;top:0;width:249px;height:187px;background:linear-gradient(90deg,var(--navy) 0%,#5c7686 30%,#a99a8c 60%,#3b5d86 100%)}
.story-rule{left:33px;top:63px;width:147px;height:3px;background:var(--orange)}
.story-quote{left:34px;top:70px;width:160px;font-family:"Alegreya",serif;font-style:italic;font-size:16px;line-height:.98;color:var(--white)}
.story-card{left:21px;top:140px;width:161px;height:60px;background:var(--white);border-radius:22px 22px 0 0}
.story-letter{left:34px;top:157px;width:148px;font-size:8.2px;line-height:1.26;color:var(--slate)}
.story-letter p{margin-bottom:10px}
.story-sign{color:var(--orange);font-style:italic}
.story-divider{left:192px;top:199px;width:1px;height:210px;background:#c9d3dc}
.unique-head{left:202px;top:198px;display:flex;align-items:center;gap:4px;font-size:13.5px;font-weight:500;color:var(--slate);letter-spacing:.3px}
.unique-head .sq{width:23px;height:14px;background:var(--orange)}
.unique-list{left:202px;top:222px;width:215px;font-size:8.2px;line-height:1.24;color:var(--slate)}
.unique-list b{display:block;color:var(--navy)}

/* Team */
.team-band{left:0;top:0;width:429px;height:78px;background:var(--navy-deep)}
.team-title{left:0;right:0;top:24px;text-align:center;font-family:"Alegreya",serif;font-weight:500;font-size:16px;color:var(--white)}
.team-diagram{left:0;top:0}
.role{font-family:"Alegreya Sans",sans-serif;font-weight:500;font-size:9.5px;fill:var(--white);letter-spacing:.3px}
.resources{left:140px;top:337px;width:155px;text-align:center;color:var(--slate);font-size:8.4px;line-height:1.15}
.resources strong{display:block;font-size:10px;font-weight:500;line-height:1.2}

/* Services */
.services-bg{left:0;top:0;width:429px;height:429px;background:linear-gradient(180deg,#b8a592 0%,#9a8676 28%,#6f7479 48%,var(--navy) 68%,var(--navy) 100%)}
.services-rule{left:52px;width:325px;height:1.5px;background:var(--white)}
.tag{height:12px;padding:0 14px 0 4px;background:var(--orange);color:var(--white);font-size:9.5px;font-weight:500;line-height:12px;letter-spacing:.3px;clip-path:polygon(0 0,100% 0,88% 100%,0 100%)}
.offer-text{left:78px;top:201px;width:140px;font-size:10.3px;line-height:1.2;color:var(--white)}
.serve-list{left:236px;top:201px;font-size:10.3px;line-height:1.2;color:var(--white);list-style:none}
.svc-head{font-size:8.4px;font-weight:500;color:var(--orange);letter-spacing:.2px}
.svc-col{font-size:8.2px;line-height:1.26;color:var(--white)}
.svc-col ul{list-style:none}
.bullet{display:inline-block;width:5px;height:4px;background:var(--orange);border-radius:4px 0 4px 0;margin-right:2px;vertical-align:1px}
.footer-brand{left:74px;top:368px;display:flex;align-items:center;gap:8px}
.footer-brand .dot{width:34px;height:34px;border-radius:50%;background:var(--orange)}
.footer-brand .brand-name{font-size:15px;width:68px;color:var(--slate)}
.contact{left:219px;top:367px;color:var(--slate)}
.contact .phone{display:flex;align-items:center;gap:5px;font-size:16px;font-weight:500}
.contact .line{display:flex;align-items:center;gap:4px;font-size:8.2px;line-height:1.3}
</style>
</head>
<body>

<section class="panel panel--cover">
  <div class="abs cover-photo" role="img" aria-label="Photo of a multi-generational family running through autumn leaves in a park, warm orange tint"></div>
  <div class="abs cover-brand">
    <span class="dot"></span>
    <span class="brand-name">Bellhaven Custodial</span>
  </div>
  <h1 class="abs cover-tagline">Helping families protect and enrich<br>a multi-generational heritage.</h1>
  <p class="abs cover-url">WWW.BELLHAVENCUSTODIAL.EXAMPLE</p>
</section>

<section class="panel panel--story">
  <div class="abs story-band"></div>
  <div class="abs story-photo" role="img" aria-label="Portrait of the founding principal in a blue blazer in an office"></div>
  <div class="abs story-rule"></div>
  <p class="abs story-quote">We believe a family “legacy” is about more than just money.</p>
  <div class="abs story-card"></div>
  <div class="abs story-letter">
    <p>We understand that wealth and families is very complex. As families try to transfer wealth it can be an incredible blessing or, if done improperly, can be incredibly destructive.</p>
    <p>Often a neutral third party is needed to come alongside the family’s advisory team to provide guidance as families go through their wealth transition.</p>
    <p>Our relational focus, and Open Architecture™ approach, helps families to successfully navigate through the complexities of wealth, family and trusts.</p>
    <p>We believe a family “legacy” is about more than just money.</p>
    <p class="story-sign">Daniel Ashford, J.D.<br>Founding Principal</p>
  </div>
  <div class="abs story-divider"></div>
  <h2 class="abs unique-head"><span class="sq"></span>WHAT MAKES BHC UNIQUE</h2>
  <div class="abs unique-list">
    <b>1. Responsive</b>The family deals directly with decision makers instead of being subject to committees with whom the family may never have the opportunity to interact or engage.
    <b>3. Independent</b>To avoid any conflicts of interest, we have no formal affiliations with wealth management firms or financial advisory practices
    <b>2. Family Focus</b>We help families successfully navigate the complexities of family wealth, not just perform trust administration.
    <b>4. Customized</b>Together we develop a customized approach that will best suit the family’s needs.
    <b>5. Collaborative</b>We work collaboratively with the family’s team of trusted professionals.
  </div>
  <div class="accent-bar"></div>
</section>

<section class="panel panel--team">
  <div class="abs team-band"></div>
  <h2 class="abs team-title">Client/Family Centered Team</h2>
  <svg class="abs team-diagram" width="429" height="429" viewBox="0 0 429 429">
    <defs>
      <linearGradient id="hexFill" x1="0" y1="0" x2="1" y2="1">
        <stop offset="0" stop-color="#f3b06a"/>
        <stop offset="1" stop-color="#d9803a"/>
      </linearGradient>
    </defs>
    <g stroke="var(--orange)" stroke-width="3">
      <line x1="217" y1="217" x2="151" y2="106"/>
      <line x1="217" y1="217" x2="281" y2="107"/>
      <line x1="217" y1="217" x2="81" y2="217"/>
      <line x1="217" y1="217" x2="348" y2="218"/>
      <line x1="217" y1="217" x2="145" y2="327"/>
      <line x1="217" y1="217" x2="297" y2="320"/>
    </g>
    <polygon points="141,217 179,151 255,151 293,217 255,283 179,283" fill="url(#hexFill)" role="img" aria-label="Photo of an older couple reviewing documents, orange tint"/>
    <text x="217" y="212" text-anchor="middle" font-family="Alegreya Sans, sans-serif" font-weight="500" font-size="18" fill="#fff">TRUST</text>
    <text x="217" y="231" text-anchor="middle" font-family="Alegreya Sans, sans-serif" font-weight="500" font-size="18" fill="#fff">CREATOR</text>
    <g fill="var(--slate)">
      <circle cx="151" cy="106" r="46"/>
      <circle cx="281" cy="107" r="46"/>
      <circle cx="81" cy="217" r="46"/>
      <circle cx="348" cy="218" r="46"/>
      <circle cx="145" cy="327" r="46"/>
    </g>
    <circle cx="297" cy="320" r="46" fill="var(--orange)"/>
    <text class="role" x="151" y="103" text-anchor="middle">CURRENT</text>
    <text class="role" x="151" y="115" text-anchor="middle">BENEFICIARY</text>
    <text class="role" x="281" y="106" text-anchor="middle">FUTURE</text>
    <text class="role" x="281" y="118" text-anchor="middle">BENEFICIARY</text>
    <text class="role" x="81" y="221" text-anchor="middle">ATTORNEY</text>
    <text class="role" x="348" y="222" text-anchor="middle">ACCOUNTANT</text>
    <text class="role" x="145" y="331" text-anchor="middle">FINANCIAL</text>
    <text class="role" x="297" y="314" text-anchor="middle">TRUSTEE</text>
  </svg>
  <div class="abs resources">
    <strong>HUMAN<br>CAPITAL<br>RESOURCES</strong>
    Legacy development<br>Health care management<br>Philanthropic services<br>Life coaching
  </div>
  <div class="accent-bar"></div>
</section>

<section class="panel panel--services">
  <div class="abs services-bg" role="img" aria-label="Photo of an advisor meeting with a smiling senior couple signing documents, fading into dark navy"></div>
  <div class="abs services-rule" style="top:179px"></div>
  <div class="abs tag" style="left:78px;top:189px">WHAT WE OFFER</div>
  <div class="abs tag" style="left:234px;top:189px">WHO WE SERVE</div>
  <p class="abs offer-text">We specialize exclusively in the delivery of trustee and estate fiduciary services.</p>
  <ul class="abs serve-list" style="top:201px">
    <li><span class="bullet"></span>Families</li>
    <li><span class="bullet"></span>Professional Advisors</li>
    <li><span class="bullet"></span>Foundations</li>
  </ul>
  <div class="abs services-rule" style="top:243px"></div>
  <div class="abs svc-col" style="left:53px;top:250px;width:200px">
    <div class="svc-head">HOW WE SERVE</div>
    Our expertise and experience is in family wealth. In this regard, we serve in the following ways:
    <ul>
      <li><span class="bullet"></span>Trustee (Trusts)</li>
      <li><span class="bullet"></span>Executor and Personal Representative (Will)</li>
      <li><span class="bullet"></span>Agent for Financial Affairs (Power of Attorney)</li>
      <li><span class="bullet"></span>Trust Protector</li>
      <li><span class="bullet"></span>Special Independent Trustee</li>
      <li><span class="bullet"></span>Consultant</li>
      <li><span class="bullet"></span>Expert Witness</li>
    </ul>
  </div>
  <div class="abs svc-col" style="left:256px;top:252px;width:125px">
    <div class="svc-head">TRUST SPECIALTIES</div>
    The general types of trusts on which we serve as trustee:
    <ul>
      <li><span class="bullet"></span>Family Trusts</li>
      <li><span class="bullet"></span>Charitable Trusts</li>
      <li><span class="bullet"></span>Family Foundations</li>
      <li><span class="bullet"></span>Life Insurance Trusts</li>
      <li><span class="bullet"></span>Retirement Trusts</li>
      <li><span class="bullet"></span>Special Needs Trusts</li>
    </ul>
  </div>
  <div class="abs footer-brand">
    <span class="dot"></span>
    <span class="brand-name">Bellhaven Custodial</span>
  </div>
  <div class="abs contact">
    <div class="phone">
      <svg width="13" height="13" viewBox="0 0 24 24" aria-hidden="true"><path fill="var(--slate)" d="M6.6 10.8a15.1 15.1 0 0 0 6.6 6.6l2.2-2.2a1 1 0 0 1 1-.25 11.4 11.4 0 0 0 3.6.57 1 1 0 0 1 1 1V20a1 1 0 0 1-1 1A17 17 0 0 1 3 4a1 1 0 0 1 1-1h3.5a1 1 0 0 1 1 1c0 1.25.2 2.45.57 3.57a1 1 0 0 1-.25 1z"/></svg>
      555-014-2290
    </div>
    <div class="line"><svg width="8" height="6" viewBox="0 0 8 6" aria-hidden="true"><rect width="8" height="6" rx="1" fill="var(--slate)"/></svg>info@bellhavencustodial.example</div>
    <div class="line"><svg width="8" height="8" viewBox="0 0 8 8" aria-hidden="true"><circle cx="4" cy="4" r="4" fill="var(--slate)"/></svg>bellhavencustodial.example</div>
  </div>
</section>

</body>
</html>
```